Established food business needs a new name card design

Refer to attached current name card. Would like a new professional look design with only the company name and logo without any pictures. Would like green and yellow to be included.
To include:
My name "HAKIM RUSLAN" and hand phone number "86207319".
To delete "
"Along Pinegrove Ave 3" and
"www.bu-tirah.com.sg"
To change email to:
"rvk27@tealmail.com.sg"

```html
<!DOCTYPE html>
<html lang="en">
<head>
<meta charset="utf-8">
<title>Bu-Tirah Name Card</title>
<link href="https://fonts.googleapis.com/css2?family=Roboto:wght@400;500;700&display=swap" rel="stylesheet">
<style>
  :root {
    --brand-green: #0c4a30;
    --brand-yellow: #f8c700;
    --paper: #ffffff;
    --pattern-cream: #fdf6dc;
    --body-grey: #555a57;
    --stage: #ecebe8;
  }
  * { box-sizing: border-box; margin: 0; padding: 0; }
  html, body {
    width: 1125px; height: 1200px; overflow: hidden;
    background: var(--stage);
    font-family: "Roboto", Arial, sans-serif;
  }
  .stage {
    position: relative;
    width: 1090px; height: 1163px;
    transform: scale(1.032);
    transform-origin: 0 0;
  }
  .card {
    position: absolute; left: 166px;
    width: 800px; height: 456px;
    background: var(--paper);
    overflow: hidden;
    box-shadow: 0 2px 6px rgba(0,0,0,0.18);
  }
  .card--front { top: 103px; }
  .card--back { top: 619px; }
  .card__shape { position: absolute; inset: 0; width: 100%; height: 100%; }
  .holder-name {
    position: absolute; left: 55px; top: 68px;
    font-size: 28px; font-weight: 700; letter-spacing: 0.3px;
    color: var(--brand-green);
  }
  .address {
    position: absolute; left: 56px; top: 240px;
    font-style: normal;
    font-size: 19px; line-height: 24px; color: var(--body-grey);
  }
  .contacts {
    position: absolute; left: 56px; top: 322px;
    list-style: none;
    font-size: 19px; line-height: 24px; color: var(--body-grey);
  }
  .contacts li { display: flex; align-items: center; gap: 12px; }
  .contacts svg { width: 19px; height: 19px; fill: var(--brand-green); flex: none; }
  .brand {
    position: absolute; left: 462px; top: 196px;
    display: flex; align-items: center; gap: 16px;
  }
  .brand__dot {
    width: 56px; height: 56px; border-radius: 50%;
    border: 5px solid var(--brand-yellow);
  }
  .brand__name {
    font-size: 40px; font-weight: 500; letter-spacing: 1px;
    color: var(--brand-yellow);
  }
  .back-field {
    position: absolute; inset: 0;
    background: radial-gradient(circle at 50% 45%, #fffdf5, var(--pattern-cream));
  }
  .back-brand {
    position: absolute; right: 58px; top: 376px;
    font-size: 24px; font-weight: 500; letter-spacing: 1px;
    color: var(--brand-yellow);
  }
</style>
</head>
<body>
<main class="stage">

  <section class="card card--front">
    <svg class="card__shape" viewBox="0 0 800 456" preserveAspectRatio="none" aria-hidden="true">
      <path d="M362 0 Q452 228 340 456 L800 456 L800 0 Z" fill="#f8c700"/>
      <path d="M370 0 Q462 228 356 456 L800 456 L800 0 Z" fill="#0c4a30"/>
      <path d="M358 0 Q440 228 338 456 L350 456 Q446 228 364 0 Z" fill="#ffffff"/>
    </svg>

    <h1 class="holder-name">HAKIM RUSLAN</h1>

    <address class="address">
      52 Tembusu Industrial<br>
      Estate Road 7 # 02-14<br>
      Singapore 648201
    </address>

    <ul class="contacts">
      <li>
        <svg viewBox="0 0 24 24" aria-hidden="true"><path d="M6.6 10.8a15.1 15.1 0 0 0 6.6 6.6l2.2-2.2c.3-.3.7-.4 1-.2 1.1.4 2.3.6 3.6.6.6 0 1 .4 1 1V20c0 .6-.4 1-1 1A17 17 0 0 1 3 4c0-.6.4-1 1-1h3.5c.6 0 1 .4 1 1 0 1.3.2 2.5.6 3.6.1.3 0 .7-.2 1z"/></svg>
        86207319
      </li>
      <li>
        <svg viewBox="0 0 24 24" aria-hidden="true"><path d="M3 5h18v14H3z M4.5 6.5 12 12l7.5-5.5v1.6L12 13.6 4.5 8.1z" fill-rule="evenodd"/></svg>
        rvk27@tealmail.com.sg
      </li>
    </ul>

    <div class="brand">
      <span class="brand__dot"></span>
      <span class="brand__name">BU-TIRAH</span>
    </div>
  </section>

  <section class="card card--back">
    <div class="back-field" role="img" aria-label="Faint repeating pattern of the brand symbol in pale yellow"></div>
    <p class="back-brand">BU-TIRAH</p>
  </section>

</main>
</body>
</html>
```